lantern productions business cards design

design a clean look but creative business card for a production company, I'm a freelance producer and launching my startup, would like to keep a clean professional look but still creative

Target Market(s)

businesses

Industry/Entity Type

video production

Contact Information for Business Card

logo, name (Mark Ellis), Title (Producer), (MFA Filmmaking, CSPT Los Angeles), contact number & email ID

Colors

Designer to choose only greyscale colors for use in the design.

Requirements
Must have
• logo, black and white colors, you can play with their shades
Nice to have
• a unique design, not necessarily a typical size card
Should not have
• too colorful or playful

```html
<!DOCTYPE html>
<html lang="en">
<head>
<meta charset="UTF-8">
<title>Lantern Productions – Business Card</title>
<link href="https://fonts.googleapis.com/css2?family=Poppins:wght@400;600&display=swap" rel="stylesheet">
<style>
  :root {
    --backdrop: #d9d9db;
    --card-light: #ffffff;
    --card-dark: #1b1d1f;
    --ink: #1a1a1a;
    --ink-soft: #6b6b6b;
    --accent: #f2b705;
    --pattern-tone: #e6e6e6;
    --mark-tone: #3a3d40;
  }
  * { margin: 0; padding: 0; box-sizing: border-box; }
  html, body {
    width: 1200px; height: 800px; overflow: hidden;
    background: var(--backdrop);
    font-family: "Poppins", sans-serif;
  }
  .canvas { position: relative; width: 1200px; height: 800px; }

  .card {
    position: absolute;
    width: 560px; height: 320px;
    border-radius: 22px;
    overflow: hidden;
    box-shadow: 0 10px 30px rgba(0,0,0,0.18);
  }

  /* Front side */
  .card-front { left: 70px; top: 90px; background: var(--card-light); }
  .front-pattern {
    position: absolute; inset: 0;
    background: linear-gradient(215deg, var(--pattern-tone) 0%, rgba(230,230,230,0.55) 40%, rgba(255,255,255,0) 72%);
  }
  .contact-block {
    position: absolute; left: 40px; bottom: 34px;
    color: var(--ink);
  }
  .person-name { font-size: 26px; font-weight: 600; line-height: 1.1; }
  .person-title { font-size: 14px; color: var(--ink-soft); margin-top: 2px; }
  .accent-rule {
    width: 26px; height: 2px; background: var(--accent);
    margin: 10px 0 8px;
  }
  .company-name { font-size: 15px; font-weight: 600; line-height: 1.3; }
  .credential { font-size: 14px; color: var(--ink-soft); line-height: 1.35; }
  .contact-list { list-style: none; }
  .contact-item {
    display: flex; align-items: center; gap: 10px;
    font-size: 14px; color: var(--ink-soft); line-height: 1.45;
  }
  .contact-icon { width: 12px; height: 12px; flex: none; fill: var(--ink); }

  /* Back side */
  .card-back {
    left: 570px; top: 390px;
    background: var(--card-dark);
    display: flex; align-items: center; justify-content: center; gap: 14px;
  }
  .brand-dot { width: 16px; height: 16px; border-radius: 50%; background: var(--mark-tone); }
  .brand-name {
    font-size: 30px; font-weight: 600; color: var(--mark-tone);
    letter-spacing: 1px; text-transform: uppercase;
  }
</style>
</head>
<body>
<main class="canvas">
  <section class="card card-front">
    <div class="front-pattern" role="img" aria-label="Faint repeating brand pattern fading toward the lower left"></div>
    <div class="contact-block">
      <h1 class="person-name">Mark Ellis</h1>
      <p class="person-title">Producer</p>
      <div class="accent-rule"></div>
      <p class="company-name">Lantern Productions</p>
      <p class="credential">MFA Filmmaking</p>
      <p class="credential">CSPT Los Angeles</p>
      <div class="accent-rule"></div>
      <ul class="contact-list">
        <li class="contact-item">
          <svg class="contact-icon" viewBox="0 0 24 24"><path d="M6.6 10.8a15 15 0 0 0 6.6 6.6l2.2-2.2a1 1 0 0 1 1-.25 11.4 11.4 0 0 0 3.6.57 1 1 0 0 1 1 1V20a1 1 0 0 1-1 1A17 17 0 0 1 3 4a1 1 0 0 1 1-1h3.5a1 1 0 0 1 1 1c0 1.25.2 2.45.57 3.57a1 1 0 0 1-.25 1z"/></svg>
          555-204-7731
        </li>
        <li class="contact-item">
          <svg class="contact-icon" viewBox="0 0 24 24"><path d="M2 5h20v14H2z M2 5l10 8 10-8" fill="none" stroke="#1a1a1a" stroke-width="2.4"/></svg>
          info@lanternprod.co
        </li>
        <li class="contact-item">
          <svg class="contact-icon" viewBox="0 0 24 24"><circle cx="12" cy="12" r="10"/></svg>
          lanternprod.co
        </li>
      </ul>
    </div>
  </section>

  <section class="card card-back">
    <span class="brand-dot"></span>
    <span class="brand-name">Lantern Productions</span>
  </section>
</main>
</body>
</html>
```